依頼詳細
瓶の容量は330mlで、茶色の瓶で、王冠はシルバーです。(瓶の写真を添付します)
アルコール度数は7%で非加熱処理なので、ドライですっきりとした飲み口のシードルです。
食中酒としてもご利用いただけます。
販売価格は650円(税込み)です。

弊社店舗のロゴも添付しますのでラベルデザインにおいてご活用ください。
また記載いただきたい文字情報として以下の情報をお取り扱いください。

商品名:Mavolt CIDER
その他1:The Genuine Brisk & Tap Hard Cider Alc.7%
その他2:APPLE 100% natural
その他2:Harvested and Brewed in HIROSAKI,AOMORI,JAPAN

記載項目
ラベルサイズは縦8センチ×横7センチくらいをを基準にご提案ください。
希望イメージ
シンプル 複雑
単色 カラフル
暗い 明るい
日常 高級
遊び心 厳粛
未来的 伝統的
女性的 男性的
希望する色
茶系
納品ファイル
• 高解像度JPG (.jpg)
• イラストレーター形式 (.ai)

視認性も非常によく、シードルの爽やかな印象をデザインに投影いただきました。

皆様、この度はたくさんのご提案まことにありがとうございます。
心より御礼申し上げます。

```html
<!DOCTYPE html>
<html lang="en">
<head>
<meta charset="utf-8">
<title>Mavolt CIDER label</title>
<link href="https://fonts.googleapis.com/css2?family=Oswald:wght@300;400&family=Roboto+Condensed:wght@400;700&family=Noto+Sans+JP:wght@500&display=swap" rel="stylesheet">
<style>
  :root {
    --page: #f2efea;
    --brick: #7c3a2c;
    --brick-soft: #8a4535;
    --cream: #f6f1e1;
    --brown: #5a3a22;
    --apple-red: #c23a32;
    --apple-soft: #d45a4c;
    --stamp-pink: #e24a7d;
    --white: #ffffff;
  }
  * { margin: 0; padding: 0; box-sizing: border-box; }
  html, body { width: 1200px; height: 2260px; overflow: hidden; background: var(--page); }
  .label {
    position: absolute; left: 80px; top: 490px; width: 1040px; height: 1275px;
    overflow: hidden;
  }
  .brick-side { position: absolute; top: 0; width: 250px; height: 1275px; }
  .brick-side--left { left: 0; }
  .brick-side--right { left: 810px; width: 230px; }
  .panel {
    position: absolute; left: 250px; top: 0; width: 560px; height: 1275px;
    background: var(--cream); color: var(--brown);
    font-family: "Roboto Condensed", sans-serif; text-align: center;
  }
  .shop-mark {
    position: absolute; left: 215px; top: 55px; width: 130px; height: 130px;
    border-radius: 50%; border: 12px solid var(--brown);
  }
  .shop-line { position: absolute; top: 205px; width: 100%; font-size: 46px; font-weight: 700; line-height: 1; }
  .product-name { position: absolute; top: 262px; width: 100%; font-size: 108px; font-weight: 700; line-height: 1; letter-spacing: 2px; }
  .product-type {
    position: absolute; top: 385px; width: 100%;
    font-family: "Oswald", sans-serif; font-weight: 300; font-size: 180px; line-height: 1; letter-spacing: 6px;
  }
  .tagline { position: absolute; top: 612px; width: 100%; font-size: 30px; line-height: 1; }
  .strength { position: absolute; top: 652px; width: 100%; font-size: 32px; font-weight: 700; line-height: 1; }
  .apple-art {
    position: absolute; left: 40px; top: 715px; width: 200px; height: 190px;
    background: linear-gradient(160deg, var(--apple-soft), var(--apple-red));
  }
  .apple-claim {
    position: absolute; left: 250px; top: 860px; width: 280px;
    font-size: 42px; line-height: 1.05; text-align: center;
  }
  .origin { position: absolute; top: 1010px; width: 100%; font-size: 36px; line-height: 1.4; }
  .alcohol-stamp {
    position: absolute; left: 790px; top: 840px; width: 200px; height: 200px; border-radius: 50%;
    background: var(--stamp-pink); color: var(--white);
    font-family: "Noto Sans JP", sans-serif; font-weight: 500; font-size: 72px; line-height: 1;
    display: flex; align-items: center; justify-content: center;
  }
  .volume {
    position: absolute; left: 880px; top: 1110px; font-size: 38px; line-height: 1; color: var(--cream);
    font-family: "Roboto Condensed", sans-serif;
  }
</style>
</head>
<body>
  <div class="label">
    <svg class="brick-side brick-side--left" viewBox="0 0 250 1275" preserveAspectRatio="none" role="img" aria-label="Red brick wall texture, left side of the label">
      <defs>
        <linearGradient id="brickTone" x1="0" y1="0" x2="0" y2="1">
          <stop offset="0" stop-color="#8a4535"/>
          <stop offset="1" stop-color="#6e3024"/>
        </linearGradient>
      </defs>
      <rect width="250" height="1275" fill="url(#brickTone)"/>
    </svg>
    <svg class="brick-side brick-side--right" viewBox="0 0 230 1275" preserveAspectRatio="none" role="img" aria-label="Red brick wall texture, right side of the label">
      <rect width="230" height="1275" fill="url(#brickTone)"/>
    </svg>
    <div class="panel">
      <div class="shop-mark"></div>
      <div class="shop-line">Café &amp; Bar</div>
      <div class="product-name">Mavolt</div>
      <div class="product-type">CIDER</div>
      <div class="tagline">The Genuine Brisk &amp; Tap Hard Cider</div>
      <div class="strength">Alc.7%</div>
      <div class="apple-art" role="img" aria-label="Photograph of a red apple with a green leaf"></div>
      <div class="apple-claim">APPLE 100%<br>natural</div>
      <div class="origin">Harvested and Brewed in<br>HIROSAKI,AOMORI,JAPAN</div>
    </div>
    <div class="alcohol-stamp">お酒</div>
    <div class="volume">330ml</div>
  </div>
</body>
</html>
```